Updated DJ business Card showing other businesses

DJ Kestro offers professional mobile dj services including DJ. MC. Karaoke.
Silent Disco (will attach logo)
I also offer a 360 Photo Booth.

Contact info:
(555) 314-7720
lenny.corbitt@mailvane.net
Social Media @DJKestroBPZ

```html
<!DOCTYPE html>
<html lang="en">
<head>
<meta charset="utf-8">
<title>DJ Kestro – Business Card</title>
<link rel="stylesheet" href="https://fonts.googleapis.com/css2?family=Share+Tech+Mono&display=swap">
<style>
  :root {
    --page-bg: #e9e7ec;
    --card-dark: #383636;
    --card-red: #d4164a;
    --photo-magenta-1: #8a1f5c;
    --photo-magenta-2: #5a1640;
    --photo-lavender-1: #d9d4e4;
    --photo-lavender-2: #a79cb8;
    --ink-white: #ffffff;
    --ink-dark: #1c1c1c;
    --shadow: rgba(0, 0, 0, 0.35);
  }
  html, body {
    margin: 0;
    padding: 0;
    width: 1200px;
    height: 1200px;
    overflow: hidden;
    background: var(--page-bg);
    font-family: "Share Tech Mono", monospace;
  }
  .canvas {
    position: relative;
    width: 1200px;
    height: 1200px;
  }
  .card {
    position: absolute;
    width: 704px;
    height: 402px;
    overflow: hidden;
    box-shadow: 8px 10px 18px var(--shadow);
  }
  .card-front { left: 110px; top: 157px; background: var(--card-dark); }
  .card-back  { left: 362px; top: 616px; background: var(--card-red); }
  .photo-area {
    position: absolute;
    inset: 0;
  }
  .brand-name {
    position: absolute;
    margin: 0;
    line-height: 1;
    letter-spacing: 1px;
    font-weight: 400;
    white-space: nowrap;
  }
  .card-front .brand-name {
    left: 319px;
    top: 136px;
    font-size: 58px;
    color: var(--ink-white);
  }
  .service-tab {
    position: absolute;
    left: 350px;
    top: 200px;
    width: 231px;
    height: 103px;
    background: var(--ink-white);
    border-radius: 0 0 34px 34px;
    display: flex;
    align-items: center;
    justify-content: center;
  }
  .service-mark {
    display: flex;
    align-items: center;
    gap: 10px;
    font-size: 24px;
    color: var(--ink-dark);
    white-space: nowrap;
  }
  .service-mark .dot {
    width: 28px;
    height: 28px;
    border-radius: 50%;
    background: var(--ink-dark);
    flex: none;
  }
  .card-back .brand-name {
    left: 28px;
    top: 50px;
    font-size: 52px;
    color: var(--ink-dark);
  }
  .card-back .service-mark {
    position: absolute;
    left: 35px;
    top: 140px;
  }
  .contact-list {
    position: absolute;
    right: 56px;
    top: 184px;
    margin: 0;
    padding: 0;
    list-style: none;
    text-align: right;
    color: var(--ink-white);
    font-size: 30px;
    line-height: 58px;
  }
  .service-list {
    position: absolute;
    left: 30px;
    bottom: 20px;
    margin: 0;
    color: var(--ink-white);
    font-size: 16px;
    letter-spacing: 0.5px;
    white-space: nowrap;
  }
</style>
</head>
<body>
<main class="canvas">

  <section class="card card-front" aria-label="Business card front">
    <svg class="photo-area" width="704" height="402" viewBox="0 0 704 402" role="img" aria-label="Photo of a DJ's hand on a mixing deck, tinted magenta">
      <defs>
        <linearGradient id="magentaPhoto" x1="0" y1="0" x2="0.6" y2="1">
          <stop offset="0" stop-color="var(--photo-magenta-1)"/>
          <stop offset="1" stop-color="var(--photo-magenta-2)"/>
        </linearGradient>
      </defs>
      <path d="M0 0 H294 C260 180 160 340 0 402 Z" fill="url(#magentaPhoto)"/>
    </svg>
    <p class="brand-name">DJ KESTRO</p>
    <div class="service-tab">
      <span class="service-mark"><span class="dot"></span>SILENT DISCO</span>
    </div>
  </section>

  <section class="card card-back" aria-label="Business card back">
    <svg class="photo-area" width="704" height="402" viewBox="0 0 704 402" role="img" aria-label="Faded photo of a DJ turntable in pale lavender tones">
      <defs>
        <linearGradient id="lavenderPhoto" x1="0" y1="0" x2="1" y2="1">
          <stop offset="0" stop-color="var(--photo-lavender-1)"/>
          <stop offset="1" stop-color="var(--photo-lavender-2)"/>
        </linearGradient>
      </defs>
      <path d="M0 0 H368 C340 150 220 240 0 232 Z" fill="url(#lavenderPhoto)"/>
    </svg>
    <p class="brand-name">DJ KESTRO</p>
    <span class="service-mark"><span class="dot"></span>SILENT DISCO</span>
    <ul class="contact-list">
      <li>@DJKestroBPZ</li>
      <li>(555) 314-7720</li>
      <li>lenny.corbitt@mailvane.net</li>
    </ul>
    <p class="service-list">DJ · MC · KARAOKE · SILENT DISCO · 360 PHOTO BOOTH</p>
  </section>

</main>
</body>
</html>
```